Nobody Left the Lantern Burning - Tom Halvery - CD Cover Design Project

Single Cover for CD & Online media e.g. Tunebox Graphics
The first song release from Tom Halvery will be the track 'Nobody Left the Lantern Burning'.
For the release the single requires artwork that is eye catching, seriously professional & meets the requirements of Disc Sprout, Tunebox and also a physical copy on CD.
Track listings for CD will be:
1. Nobody Left the Lantern Burning
2. Nobody Left the Lantern Burning - Instrumental
see details in this link:
http://members.discsprout-example.com/faq.aspx
http://selfmadesound.discsprout-example.com/2009/11/avoid-album-art-atrocities/
http://answers.quorvex-example.com/question/index?qid=20111015141433AAdDTmH
Any advice on this would be greatly appreciated,
I would also like the two logo's I have uploaded to be used,
one is the Tom Halvery logo and the other is for Milbrook & Tandy Records logo (please remove the R and replace with a C for copyright.)
There are four high res photo shopped pictures of Tom Halvery and another zip file of many others, it would be nice to include one of these maybe on the 2nd page or back of the CD. Please don't use them as the front cover.
I imagine an Art Deco illustration but please listen to the track and let it inspire you.
Good Luck
Updates
I don't feel this is what I'm looking for, the design needs to refelct a broken heart without being a picture of a broken heart
Reason: No design has been what we are after so far so the deadline has been extended and the budget increased.

```html
<!DOCTYPE html>
<html lang="en">
<head>
<meta charset="utf-8">
<title>Nobody Left the Lantern Burning – Tom Halvery – CD Artwork</title>
<link href="https://fonts.googleapis.com/css2?family=Oswald:wght@500;700&display=swap" rel="stylesheet">
<style>
  :root {
    --backdrop: #ffffff;
    --paper: #ecdcb8;
    --paper-edge: #dcc79d;
    --ink: #a4381f;
    --stain: rgba(150, 95, 45, 0.28);
    --photo-dark: #8c5a35;
    --photo-light: #c99a6a;
  }
  * { box-sizing: border-box; margin: 0; padding: 0; }
  html, body { width: 1200px; height: 824px; overflow: hidden; background: var(--backdrop); }
  body { position: relative; font-family: "Oswald", "Arial Narrow", sans-serif; color: var(--ink); }

  .panel {
    position: absolute;
    background: radial-gradient(ellipse at 40% 40%, var(--paper) 55%, var(--paper-edge) 100%);
    overflow: hidden;
  }
  .rings { position: absolute; inset: 0; width: 100%; height: 100%; pointer-events: none; }

  /* Front cover */
  .front-cover { left: 80px; top: 60px; width: 320px; height: 320px; }
  .front-cover .stamp {
    position: absolute; left: 92px; top: 130px;
    transform: rotate(-42deg); transform-origin: center;
    display: flex; align-items: center; gap: 8px;
  }
  .stamp .mark { width: 30px; height: 30px; background: var(--ink); flex: none; }
  .stamp .artist { font-weight: 700; font-size: 22px; line-height: 1; text-transform: uppercase; }
  .stamp .title { font-weight: 700; font-size: 13px; line-height: 1.1; text-transform: uppercase; width: 130px; }

  /* Back tray card */
  .back-card { left: 440px; top: 70px; width: 350px; height: 310px; }
  .artist-mark {
    position: absolute; right: 18px; top: 16px;
    display: flex; align-items: center; gap: 5px;
    font-weight: 700; font-size: 12px; text-transform: uppercase;
  }
  .artist-mark .square { width: 12px; height: 12px; background: var(--ink); }
  .label-mark {
    position: absolute; left: 16px; bottom: 14px;
    display: flex; align-items: center; gap: 5px;
    font-weight: 500; font-size: 8px; text-transform: uppercase; line-height: 1.1;
  }
  .label-mark .dot { width: 12px; height: 12px; border-radius: 50%; background: var(--ink); flex: none; }

  .tracklist { list-style: none; font-weight: 700; text-transform: uppercase; }
  .tracklist li { display: flex; gap: 8px; }
  .tracklist .num { width: 18px; }
  .tracklist .note { font-size: 6px; font-weight: 500; }
  .tracklist .credit { display: block; font-size: 6px; font-weight: 500; letter-spacing: 0.02em; }
  .tracklist .time { margin-left: auto; }

  .back-card .tracklist { position: absolute; left: 95px; top: 135px; font-size: 9px; }
  .back-card .tracklist li { margin-bottom: 6px; }

  /* Inside booklet */
  .booklet { left: 160px; top: 455px; width: 300px; height: 300px; }
  .booklet .tracklist { position: absolute; left: 60px; top: 35px; width: 220px; font-size: 8px; }
  .booklet .tracklist li { margin-bottom: 6px; }
  .portrait {
    position: absolute; left: 55px; top: 140px; width: 120px; height: 120px;
    border-radius: 46% 54% 40% 60% / 52% 44% 56% 48%;
    background: radial-gradient(ellipse at 50% 45%, var(--photo-light), var(--photo-dark));
    opacity: 0.85;
  }
  .copyright { position: absolute; left: 10px; bottom: 8px; font-size: 5px; font-weight: 500; text-transform: uppercase; }

  /* Tray inlay */
  .tray-inlay { left: 460px; top: 455px; width: 300px; height: 300px; }

  /* Disc */
  .disc {
    position: absolute; left: 845px; top: 145px; width: 250px; height: 250px; border-radius: 50%;
    background: radial-gradient(circle at 45% 40%, var(--paper) 60%, var(--paper-edge) 100%);
    overflow: hidden;
  }
  .disc .hub {
    position: absolute; left: 95px; top: 95px; width: 60px; height: 60px; border-radius: 50%;
    border: 8px solid var(--stain);
  }
  .disc .hole {
    position: absolute; left: 112px; top: 112px; width: 26px; height: 26px; border-radius: 50%;
    background: var(--backdrop); box-shadow: inset 0 0 0 3px var(--paper-edge);
  }
  .disc .artist-mark { right: auto; left: 108px; top: 22px; flex-direction: column; font-size: 10px; gap: 3px; }
  .disc .label-mark { left: 30px; top: 90px; bottom: auto; font-size: 6px; }
  .disc .tracklist { position: absolute; left: 55px; top: 170px; width: 160px; font-size: 6.5px; }
  .disc .tracklist li { margin-bottom: 4px; }
</style>
</head>
<body>

<section class="panel front-cover" aria-label="Front cover">
  <svg class="rings" viewBox="0 0 320 320" aria-hidden="true">
    <circle cx="120" cy="120" r="48" fill="none" stroke="var(--stain)" stroke-width="5"/>
    <circle cx="200" cy="118" r="52" fill="none" stroke="var(--stain)" stroke-width="4"/>
    <circle cx="260" cy="255" r="10" fill="var(--stain)"/>
  </svg>
  <div class="stamp">
    <span class="mark"></span>
    <div>
      <div class="artist">Tom Halvery</div>
      <div class="title">Nobody Left the Lantern Burning</div>
    </div>
  </div>
</section>

<section class="panel back-card" aria-label="Back tray card">
  <svg class="rings" viewBox="0 0 350 310" aria-hidden="true">
    <circle cx="62" cy="85" r="9" fill="var(--stain)"/>
    <circle cx="250" cy="230" r="12" fill="var(--stain)"/>
    <circle cx="322" cy="240" r="38" fill="none" stroke="var(--stain)" stroke-width="4"/>
  </svg>
  <div class="artist-mark"><span class="square"></span>Tom Halvery</div>
  <ol class="tracklist">
    <li><span class="num">01.</span><span>Nobody Left the Lantern Burning</span></li>
    <li><span class="num">02.</span><span>Nobody Left the Lantern Burning <span class="note">(Instrumental)</span></span></li>
  </ol>
  <div class="label-mark"><span class="dot"></span>Milbrook &amp; Tandy<br>Records 2012</div>
</section>

<section class="disc" aria-label="Disc face">
  <div class="hub"></div>
  <div class="hole"></div>
  <div class="artist-mark"><span class="square"></span>Tom Halvery</div>
  <div class="label-mark"><span class="dot"></span>Milbrook &amp; Tandy<br>Records 2012</div>
  <ol class="tracklist">
    <li><span class="num">01.</span><span>Nobody Left the Lantern Burning<span class="credit">Composed, written &amp; arranged by Tom Halvery</span></span></li>
    <li><span class="num">02.</span><span>Nobody Left the Lantern Burning <span class="note">(Instrumental)</span><span class="credit">Composed, written &amp; arranged by Tom Halvery</span></span></li>
  </ol>
</section>

<section class="panel booklet" aria-label="Inside booklet">
  <ol class="tracklist">
    <li><span class="num">01.</span><span>Nobody Left the Lantern Burning<span class="credit">Composed, written &amp; arranged by Tom Halvery</span></span><span class="time">3:23</span></li>
    <li><span class="num">02.</span><span>Nobody Left the Lantern Burning <span class="note">(Instrumental)</span><span class="credit">Composed &amp; arranged by Tom Halvery</span></span><span class="time">3:23</span></li>
  </ol>
  <div class="portrait" role="img" aria-label="Sepia portrait photograph of the artist inside a coffee-stain shaped frame"></div>
  <p class="copyright">© 2012 Milbrook &amp; Tandy Records</p>
</section>

<section class="panel tray-inlay" aria-label="Tray inlay">
  <svg class="rings" viewBox="0 0 300 300" aria-hidden="true">
    <circle cx="150" cy="150" r="30" fill="none" stroke="var(--stain)" stroke-width="5"/>
  </svg>
</section>

</body>
</html>
```